We need a web site design that is connected to Talbrook Roofing an American company, Veteran owned. Specializing in new roofs of all kinds, repair existing roofs and emergency roof repairs. located in the north Georgia mountains

Target Market(s)

homeowners end users, real estate, home owners insurance companies

Industry/Entity Type

roofing

Contact Information for Business Card

logo, Veteran owned, supports veteran charities, phone number ect

Font styles to use
Serif

Requirements
Should not have
• na

```html
<!DOCTYPE html>
<html lang="en">
<head>
<meta charset="utf-8">
<title>Talbrook Roofing – Business Cards</title>
<link href="https://fonts.googleapis.com/css2?family=Montserrat:wght@400;500;700&display=swap" rel="stylesheet">
<style>
  :root{
    --stage:#2b2b2b;
    --card:#000000;
    --ink:#ffffff;
    --flame:#e8400c;
    --flame-deep:#c92a06;
    --gold:#f2b33d;
    --gold-deep:#c98a1c;
    --rule:#d9d9d9;
  }
  *{margin:0;padding:0;box-sizing:border-box}
  html,body{width:1200px;height:875px;overflow:hidden;background:var(--stage)}
  body{font-family:"Montserrat",sans-serif;color:var(--ink);position:relative}

  .card{
    position:absolute;left:280px;width:640px;height:366px;
    background:var(--card);border-radius:22px;overflow:hidden;
    box-shadow:0 14px 30px rgba(0,0,0,.55);
  }
  .card--back{top:50px}
  .card--front{top:459px}

  /* brand name stand-in */
  .brand{display:flex;align-items:center;gap:12px;position:absolute}
  .brand__dot{width:18px;height:18px;border-radius:50%;background:var(--flame)}
  .brand__name{font-weight:700;color:var(--gold);letter-spacing:.04em}

  .card--back .brand{left:0;right:0;top:120px;justify-content:center}
  .card--back .brand__name{font-size:44px}
  .tagline{
    position:absolute;left:0;right:0;top:250px;text-align:center;
    font-size:23px;font-weight:500;letter-spacing:.01em;
  }
  .tagline span{margin:0 6px}

  .card--front .brand{right:34px;top:48px}
  .card--front .brand__name{font-size:27px}
  .rule{position:absolute;height:1px;background:var(--rule)}
  .rule--top{left:250px;right:34px;top:112px}
  .rule--mid{left:44px;width:300px;top:236px}

  .person{position:absolute;left:44px;top:170px}
  .person__name{font-size:26px;font-weight:700;color:var(--flame)}
  .person__role{font-size:15px;margin-top:2px}

  .contact{position:absolute;left:44px;top:250px;list-style:none;font-size:15px}
  .contact li{display:flex;align-items:center;gap:12px;height:28px}
  .contact svg{width:16px;height:16px;flex:none}

  .address{position:absolute;right:34px;top:128px;text-align:right;font-size:14.5px;line-height:1.6}

  .band{position:absolute;left:0;bottom:0;width:640px;height:110px}
  .web{position:absolute;right:34px;bottom:14px;font-size:15px;font-weight:500}
</style>
</head>
<body>

<section class="card card--back" aria-label="Card back">
  <div class="brand">
    <span class="brand__dot"></span>
    <span class="brand__name">Talbrook Roofing</span>
  </div>
  <p class="tagline"><span>•</span>Veteran owned<span>•</span>Supports veteran charities</p>
</section>

<section class="card card--front" aria-label="Card front">
  <div class="brand">
    <span class="brand__dot"></span>
    <span class="brand__name">Talbrook Roofing</span>
  </div>
  <div class="rule rule--top"></div>

  <div class="address">58, Ridge Hollow Road<br>30512, Blairsville GA</div>

  <div class="person">
    <p class="person__name">Daniel Hartley</p>
    <p class="person__role">Owner</p>
  </div>
  <div class="rule rule--mid"></div>

  <ul class="contact">
    <li>
      <svg viewBox="0 0 24 24"><path fill="var(--gold)" d="M6.6 10.8a15 15 0 0 0 6.6 6.6l2.2-2.2a1 1 0 0 1 1-.25 11.4 11.4 0 0 0 3.6.57 1 1 0 0 1 1 1V20a1 1 0 0 1-1 1A17 17 0 0 1 3 4a1 1 0 0 1 1-1h3.5a1 1 0 0 1 1 1c0 1.25.2 2.45.57 3.57a1 1 0 0 1-.25 1z"/></svg>
      706-555 018 342
    </li>
    <li>
      <svg viewBox="0 0 24 24"><path fill="var(--gold)" d="M2 5h20v14H2z"/><path fill="none" stroke="#000" stroke-width="1.6" d="M2 5l10 8 10-8"/></svg>
      info@talbrookroof.com
    </li>
  </ul>

  <svg class="band" viewBox="0 0 640 110" preserveAspectRatio="none" aria-hidden="true">
    <polygon points="0,104 440,104 460,84 640,84 640,110 0,110" fill="var(--flame-deep)"/>
    <polygon points="0,96 428,96 446,78 456,78 436,100 0,100" fill="var(--gold)"/>
    <polygon points="462,78 640,78 640,110 430,110" fill="var(--flame)"/>
  </svg>
  <p class="web">www.talbrookroof.com</p>
</section>

</body>
</html>
```